Steadfast Valve Works

I need a business card with the attached logo.
The second page I have attached is what we are looking for. We want doubles sided. We would like the blues fading and the logo on the back.

Industry/Entity Type

Business

```html
<!DOCTYPE html>
<html lang="en">
<head>
<meta charset="utf-8">
<title>Steadfast Valve Works – Business Card</title>
<link rel="stylesheet" href="https://fonts.googleapis.com/css2?family=Open+Sans:wght@400;600;700&display=swap">
<style>
  :root {
    --stage: #d9dbde;
    --blue-deep: #0a2f6b;
    --blue-mid: #0d4a9e;
    --blue-light: #1a5bb8;
    --brand-blue: #0d3f8f;
    --ink: #222428;
    --rule: #3a3d42;
    --paper: #ffffff;
    --paper-shade: #e6e8eb;
    --white: #ffffff;
  }
  * { box-sizing: border-box; margin: 0; padding: 0; }
  html, body { width: 1200px; height: 900px; overflow: hidden; }
  body {
    background: var(--stage);
    font-family: "Open Sans", Arial, sans-serif;
    display: flex;
    flex-direction: column;
    align-items: center;
    justify-content: center;
    gap: 34px;
  }
  .card {
    position: relative;
    width: 700px;
    height: 400px;
    border-radius: 26px;
    overflow: hidden;
  }

  /* Back side */
  .card-back { color: var(--white); }
  .card-back .backdrop {
    position: absolute; inset: 0;
    background:
      linear-gradient(115deg, rgba(255,255,255,0.06) 0 38%, transparent 38% 62%, rgba(0,0,0,0.08) 62%),
      linear-gradient(160deg, var(--blue-light) 0%, var(--blue-mid) 45%, var(--blue-deep) 100%);
  }
  .card-back .brand-name {
    position: absolute;
    left: 0; right: 0; top: 160px;
    text-align: center;
    font-weight: 700;
    font-size: 42px;
    letter-spacing: 3px;
    text-transform: uppercase;
    color: var(--white);
  }
  .card-back .website {
    position: absolute;
    right: 120px; top: 236px;
    font-size: 16px;
    font-weight: 400;
  }
  .card-back .website strong { font-weight: 700; }

  /* Front side */
  .card-front { color: var(--ink); }
  .card-front .backdrop {
    position: absolute; inset: 0;
    background: radial-gradient(ellipse at 40% 30%, var(--paper) 0%, var(--paper) 45%, var(--paper-shade) 100%);
  }
  .card-front .brand-name {
    position: absolute;
    right: 44px; top: 50px;
    font-weight: 700;
    font-size: 30px;
    letter-spacing: 2px;
    text-transform: uppercase;
    color: var(--brand-blue);
  }
  .card-front .divider {
    position: absolute;
    left: 250px; right: 44px; top: 226px;
    height: 1px;
    background: var(--rule);
  }
  .card-front .address {
    position: absolute;
    right: 44px; top: 240px;
    text-align: right;
    font-size: 17px;
    line-height: 1.35;
  }
  .card-front .person {
    position: absolute;
    left: 44px; top: 184px;
  }
  .person .name {
    font-size: 22px;
    font-weight: 700;
    color: var(--brand-blue);
    line-height: 1.3;
  }
  .person .title {
    font-size: 17px;
    line-height: 1.3;
    margin-top: 2px;
  }
  .contact-list {
    list-style: none;
    margin-top: 12px;
    font-size: 18px;
    line-height: 1.55;
  }
  .contact-list li { display: flex; align-items: center; gap: 10px; }
  .contact-list svg { width: 18px; height: 18px; flex: none; fill: var(--brand-blue); }
</style>
</head>
<body>

  <section class="card card-back">
    <div class="backdrop" role="img" aria-label="Fading blue background with soft diagonal tonal bands"></div>
    <div class="brand-name">Steadfast Valve Works</div>
    <div class="website">www.<strong>SteadfastValveWorks</strong>.com</div>
  </section>

  <section class="card card-front">
    <div class="backdrop" role="img" aria-label="White card surface with faint grey shading"></div>
    <div class="brand-name">Steadfast Valve Works</div>
    <div class="divider"></div>
    <div class="address">48 Harbor Lane<br>Millbrook, Ohio<br>44870</div>
    <div class="person">
      <div class="name">Daniel Marlow</div>
      <div class="title">managing director</div>
      <ul class="contact-list">
        <li>
          <svg viewBox="0 0 24 24" aria-hidden="true"><path d="M6.6 10.8a15.1 15.1 0 0 0 6.6 6.6l2.2-2.2a1 1 0 0 1 1-.25 11.4 11.4 0 0 0 3.6.57 1 1 0 0 1 1 1V20a1 1 0 0 1-1 1A17 17 0 0 1 3 4a1 1 0 0 1 1-1h3.5a1 1 0 0 1 1 1c0 1.25.2 2.45.57 3.6a1 1 0 0 1-.25 1z"/></svg>
          610 555 0142
        </li>
        <li>
          <svg viewBox="0 0 24 24" aria-hidden="true"><path d="M7 1h10a2 2 0 0 1 2 2v18a2 2 0 0 1-2 2H7a2 2 0 0 1-2-2V3a2 2 0 0 1 2-2zm0 3v14h10V4zm5 15.5a1 1 0 1 0 0 2 1 1 0 0 0 0-2z"/></svg>
          610 555 0187
        </li>
        <li>
          <svg viewBox="0 0 24 24" aria-hidden="true"><path d="M2 5h20v14H2zm2 2v.5l8 5 8-5V7zm0 2.9V17h16V9.9l-8 5z"/></svg>
          dmarlow@steadfastvalveworks.com
        </li>
      </ul>
    </div>
  </section>

</body>
</html>
```